Larchmere Valley College

We are looking to update our current webpage at www.larchmerevalley.ca. We would like to make it modern, fresh and appealing to students. We want to keep our logo the same with the logo colours blended in as the primary colours and focus. We are open to reconfiguring content as well.
Reason: Hi, In the next 3 days we will have narrowed our search to 3 designs and will make a choice before the final deadline...
Industry/Entity Type
College

```html
<!DOCTYPE html>
<html lang="en">
<head>
<meta charset="utf-8">
<title>Larchmere Valley College</title>
<link href="https://fonts.googleapis.com/css2?family=Open+Sans:wght@300;400;600;700&display=swap" rel="stylesheet">
<style>
:root{
  --navy:#1c2b5f;
  --navy-deep:#121c44;
  --teal:#0f6d63;
  --teal-band:#0c5b53;
  --teal-light:#17867a;
  --accent:#e3245a;
  --grey:#8a8f94;
  --grey-light:#c9ccce;
  --line:#e3e5e6;
  --white:#ffffff;
}
*{box-sizing:border-box;margin:0;padding:0}
html,body{width:1200px;height:2353px;overflow:hidden;background:var(--white);font-family:"Open Sans",Arial,sans-serif;color:#333}
.page{position:relative;width:1200px;height:2353px}
.abs{position:absolute}

.utility-links{top:4px;right:30px;font-size:14px;color:var(--grey)}
.brand{top:34px;left:0;width:1200px;text-align:center;font-size:40px;font-weight:700;color:var(--navy);letter-spacing:.5px;line-height:80px}

.main-nav{top:144px;left:0;width:1200px;height:40px;border-top:1px solid var(--line);border-bottom:1px solid var(--line)}
.menu-toggle{left:108px;top:12px;width:22px;height:16px;display:flex;flex-direction:column;justify-content:space-between}
.menu-toggle span{display:block;height:3px;background:var(--navy)}
.social-list{right:112px;top:13px;display:flex;gap:11px}
.social-list span{width:13px;height:13px;border-radius:50%;background:var(--navy)}

.hero{top:188px;left:0;width:1200px;height:576px;background:linear-gradient(135deg,#d9d4cc 0%,#b8aa98 35%,#6c625a 60%,#3a3432 100%)}
.hero-arrow{top:405px;width:104px;height:105px;background:var(--navy);display:flex;align-items:center;justify-content:center}
.hero-arrow.prev{left:0}
.hero-arrow.next{right:0;background:linear-gradient(90deg,#3d6e68 0 38%,var(--navy) 38%)}
.hero-progress{top:760px;left:0;width:470px;height:4px;background:var(--accent)}

.welcome-title{top:806px;left:0;width:1200px;text-align:center;font-size:27px;font-weight:400;color:var(--teal)}
.welcome-text{top:850px;left:220px;width:760px;text-align:center;font-size:15px;line-height:22px;color:var(--grey);font-weight:300}

.pillar{top:940px;width:240px;text-align:center}
.pillar svg{display:block;margin:0 auto}
.pillar h3{margin-top:14px;font-size:25px;font-weight:400;color:var(--teal)}

.video-band{top:1150px;left:0;width:1200px;height:398px;background:radial-gradient(ellipse at 50% 0%,#3c5196 0%,#24346e 45%,var(--navy-deep) 100%)}
.video-player{top:1256px;left:105px;width:366px;height:222px;background:linear-gradient(160deg,#7d9ab8 0%,#8aa47e 55%,#4d6b44 100%)}
.player-controls{left:0;bottom:0;width:100%;height:22px;background:#111;display:flex;align-items:center;padding:0 8px;gap:8px}
.player-controls .bar{flex:1;height:4px;background:#555}
.play-button{top:78px;left:150px;width:66px;height:66px;border-radius:50%;background:rgba(0,0,0,.45);display:flex;align-items:center;justify-content:center}
.video-title{top:1282px;left:490px;font-size:24px;color:var(--white);font-weight:400;white-space:nowrap}
.video-thumbs{top:1346px;left:478px;display:flex;gap:8px}
.video-thumbs div{width:149px;height:81px;background:linear-gradient(180deg,#e8e9eb 0%,#c3c6ca 60%,#5d626a 100%)}
.carousel-dots{top:1446px;left:760px;display:flex;gap:6px}
.carousel-dots span{width:10px;height:10px;border-radius:50%;background:#2f8f86}
.carousel-dots span.on{width:22px;border-radius:5px;background:#3fb3a6}

.info-band{top:1548px;left:0;width:1200px;height:444px;background:var(--teal-band)}
.news-panel{top:1615px;left:110px;width:432px;height:326px;background:linear-gradient(90deg,var(--teal-light) 0 100px,var(--white) 100px);box-shadow:0 3px 10px rgba(0,0,0,.3);overflow:hidden}
.news-item{position:absolute;left:0;width:100%;height:98px;display:flex}
.news-date{width:100px;height:100%;color:var(--white);padding:12px 10px;border-bottom:1px solid rgba(255,255,255,.25)}
.news-date strong{display:block;font-size:32px;font-weight:400;line-height:34px}
.news-date small{font-size:14px}
.news-body{flex:1;padding:9px 14px;font-size:11px;line-height:14px;color:#555;position:relative}
.news-body b{color:var(--teal);font-weight:700}
.news-body .more{position:absolute;right:14px;bottom:6px;color:var(--teal);font-weight:600}
.news-pager{right:0;bottom:0;display:flex}
.news-pager span{width:30px;height:26px;background:var(--teal-light);display:flex;align-items:center;justify-content:center}
.news-pager span+span{background:var(--white);border:1px solid var(--line)}

.links-panel{top:1615px;left:659px;width:426px;height:298px;background:var(--white);box-shadow:0 3px 10px rgba(0,0,0,.3);list-style:none}
.links-panel li{height:42px;display:flex;align-items:center;padding:0 18px;font-size:14px;color:var(--grey-light);border-bottom:1px solid var(--line);gap:18px}
.links-panel li:first-child{color:var(--teal);font-weight:600}
.links-panel li i{width:18px;height:18px;border-radius:50%;background:var(--grey-light);display:block}
.links-panel li:first-child i{background:var(--teal)}

.scroll-tab{top:1968px;left:582px;width:36px;height:24px;background:var(--white);border-radius:18px 18px 0 0;display:flex;align-items:center;justify-content:center}

.footer-mark{top:2118px;left:0;width:1200px;text-align:center;font-size:30px;font-weight:700;color:#e4e6e8}
</style>
</head>
<body>
<div class="page">
  <div class="abs utility-links">Apply today | Donate | Library | Info</div>
  <div class="abs brand">Larchmere Valley College</div>

  <nav class="abs main-nav">
    <div class="abs menu-toggle"><span></span><span></span><span></span></div>
    <div class="abs social-list"><span></span><span></span><span></span><span></span><span></span><span></span><span></span></div>
  </nav>

  <section class="abs hero" role="img" aria-label="Lecturer teaching students in a bright classroom"></section>
  <div class="abs hero-arrow prev"><svg width="30" height="50" viewBox="0 0 30 50"><polyline points="24,4 6,25 24,46" fill="none" stroke="#fff" stroke-width="2"/></svg></div>
  <div class="abs hero-arrow next"><svg width="30" height="50" viewBox="0 0 30 50" style="margin-left:40px"><polyline points="6,4 24,25 6,46" fill="none" stroke="#fff" stroke-width="2"/></svg></div>
  <div class="abs hero-progress"></div>

  <h1 class="abs welcome-title">Thank-you for your interest in Larchmere Valley College!</h1>
  <p class="abs welcome-text">I hope that your visit here will answer some of your questions as you consider a course of study that is right for you. Whether you are interested in pastoral ministry, counseling, missions and cross-cultural communication, theology.</p>

  <div class="abs pillar" style="left:128px">
    <svg width="80" height="80" viewBox="0 0 80 80"><path d="M10 58 Q25 50 40 58 Q55 50 70 58 L70 68 Q55 60 40 68 Q25 60 10 68Z" fill="none" stroke="#0f6d63" stroke-width="3"/><line x1="40" y1="58" x2="40" y2="68" stroke="#0f6d63" stroke-width="3"/><circle cx="30" cy="30" r="4" fill="#0f6d63"/><circle cx="46" cy="20" r="4" fill="#0f6d63"/><circle cx="54" cy="38" r="3" fill="#0f6d63"/><circle cx="36" cy="44" r="3" fill="#0f6d63"/><circle cx="24" cy="14" r="3" fill="#0f6d63"/></svg>
    <h3>Educate</h3>
  </div>
  <div class="abs pillar" style="left:481px">
    <svg width="80" height="80" viewBox="0 0 80 80"><path d="M24 12 Q60 8 68 40 Q48 40 36 46Z" fill="#0f6d63"/><rect x="32" y="46" width="6" height="16" fill="#0f6d63"/><rect x="20" y="62" width="32" height="10" rx="2" fill="#0f6d63"/></svg>
    <h3>Equiping</h3>
  </div>
  <div class="abs pillar" style="left:826px">
    <svg width="80" height="80" viewBox="0 0 80 80"><path d="M40 20 A16 16 0 0 1 50 48 L50 58 L30 58 L30 48 A16 16 0 0 1 40 20Z" fill="none" stroke="#0f6d63" stroke-width="3"/><line x1="32" y1="64" x2="48" y2="64" stroke="#0f6d63" stroke-width="3"/><line x1="34" y1="70" x2="46" y2="70" stroke="#0f6d63" stroke-width="3"/><g stroke="#0f6d63" stroke-width="3"><line x1="40" y1="4" x2="40" y2="12"/><line x1="16" y1="14" x2="21" y2="19"/><line x1="64" y1="14" x2="59" y2="19"/><line x1="6" y1="36" x2="14" y2="36"/><line x1="66" y1="36" x2="74" y2="36"/></g></svg>
    <h3>Enriching</h3>
  </div>

  <section class="abs video-band" role="img" aria-label="Wall of video screens in deep blue light"></section>
  <div class="abs video-player">
    <div class="abs" style="inset:0 0 22px 0" role="img" aria-label="Campus entrance sign video still"></div>
    <div class="abs play-button"><svg width="26" height="30" viewBox="0 0 26 30"><polygon points="2,2 24,15 2,28" fill="#fff"/></svg></div>
    <div class="abs player-controls"><svg width="10" height="12"><polygon points="0,0 10,6 0,12" fill="#fff"/></svg><span class="bar"></span></div>
  </div>
  <h2 class="abs video-title">Visit Larchmere's ViewStream channel for more videos</h2>
  <div class="abs video-thumbs">
    <div role="img" aria-label="Faculty video thumbnail"></div>
    <div role="img" aria-label="Faculty video thumbnail"></div>
    <div role="img" aria-label="Faculty video thumbnail"></div>
    <div role="img" aria-label="Faculty video thumbnail"></div>
  </div>
  <div class="abs carousel-dots"><span></span><span class="on"></span><span></span><span></span></div>

  <section class="abs info-band"></section>
  <div class="abs news-panel">
    <div class="news-item" style="top:0">
      <div class="news-date"><strong>19th</strong><small>May 2014</small></div>
      <div class="news-body"><b>ORBIT</b> Global outreach training now open for fall enrolment with mission placement and discipleship courses for new students.<span class="more">read more...</span></div>
    </div>
    <div class="news-item" style="top:98px">
      <div class="news-date"><strong>19th</strong><small>May 2014</small></div>
      <div class="news-body"><b>"Not for Profit"</b> Organizational Leadership is a four year B.A. program which focuses on leadership preparation for work in non-profit or mission agencies.<span class="more">read more...</span></div>
    </div>
    <div class="news-item" style="top:196px">
      <div class="news-date"><strong>19th</strong><small>May 2014</small></div>
      <div class="news-body"><b>Larchmere Valley</b> College is pleased to offer a one year program that is geared towards equipping a music student with skills for sound production and media.<span class="more">read more...</span></div>
    </div>
    <div class="abs news-pager">
      <span><svg width="8" height="12"><polyline points="7,1 2,6 7,11" fill="none" stroke="#fff" stroke-width="2"/></svg></span>
      <span><svg width="8" height="12"><polyline points="1,1 6,6 1,11" fill="none" stroke="#17867a" stroke-width="2"/></svg></span>
    </div>
  </div>

  <ul class="abs links-panel">
    <li><i></i>Download the full Catalogue</li>
    <li><i></i>Apply Today (Application Package)</li>
    <li><i></i>Information Request</li>
    <li><i></i>Browse our Programs</li>
    <li><i></i>Download Forms</li>
    <li><i></i>Admissions Information</li>
    <li><i></i>Campus Directory</li>
  </ul>

  <div class="abs scroll-tab"><svg width="12" height="10"><polyline points="1,8 6,3 11,8" fill="none" stroke="#0c5b53" stroke-width="2"/></svg></div>

  <div class="abs footer-mark">Larchmere Valley College</div>
</div>
</body>
</html>
```